Sales Website Design

Create a sales-oriented website to advertise turn-key solutions for providing infection control to senior housing operators. There are several items uploaded. The pdf should serve as your guide. The powerpoint presentation has additional information.

The idea is this is senior housing reimagined for infection control. The design should be sleek, clean, vibrant and energetic.

Our goal is to sell a turnkey solution for making buildings safer for residents, staff, and families.

Target Market(s)

People who own and operate senior housing communities

Coding

Coded - Design and coding required

Number of Pages Required

5+ page

```html
<!DOCTYPE html>
<html lang="en">
<head>
<meta charset="utf-8">
<title>Larkspur – Customized Solutions</title>
<link href="https://fonts.googleapis.com/css2?family=Roboto:wght@300;400;500;700&family=Open+Sans:wght@400;600&display=swap" rel="stylesheet">
<style>
:root{
  --orange:#f0592a;
  --dark:#333333;
  --darker:#262626;
  --ink:#2c2c2c;
  --muted:#6b6b6b;
  --line:#d8d8d8;
  --light:#f0f0f0;
  --white:#ffffff;
}
*{box-sizing:border-box;margin:0;padding:0}
html,body{width:1200px;height:4288px;overflow:hidden}
body{font-family:"Open Sans",Arial,sans-serif;color:var(--ink);background:var(--white)}
.page{position:relative;width:1200px;height:4288px;overflow:hidden}
.abs{position:absolute}
h1,h2,h3,.brand{font-family:"Roboto",Arial,sans-serif}
.btn{display:inline-block;background:var(--orange);color:#fff;font-family:"Roboto",Arial,sans-serif;font-size:15px;border-radius:22px;padding:11px 26px;text-decoration:none}

/* header */
.site-header{top:0;left:0;width:1200px;height:88px;background:#fff;box-shadow:0 2px 6px rgba(0,0,0,.08);z-index:5}
.brand{position:absolute;left:44px;top:26px;display:flex;align-items:center;gap:12px;font-size:30px;font-weight:500;letter-spacing:5px;color:var(--dark)}
.brand .mark{width:22px;height:22px;background:var(--orange)}
.main-nav{position:absolute;left:330px;top:35px;display:flex;gap:22px;font-family:"Roboto",sans-serif;font-size:13px;font-weight:500;color:var(--dark);white-space:nowrap}
.header-cta{position:absolute;right:40px;top:24px;padding:10px 30px;font-size:14px}

/* hero */
.hero{top:88px;left:0;width:1200px;height:632px;background:linear-gradient(180deg,#dbe8f2 0%,#eef3f6 38%,#a9b3ae 60%,#6f7d6f 78%,#9aa391 100%)}
.hero-title{top:110px;width:1200px;text-align:center;font-size:48px;font-weight:500;color:var(--dark)}
.hero-sub{top:180px;width:1200px;text-align:center;font-family:"Roboto",sans-serif;font-size:22px;font-weight:500;color:var(--dark)}
.hero-btn{top:240px;left:535px}
.arrow{width:44px;height:44px;border-radius:50%;background:var(--orange);top:262px}

/* intro */
.intro{top:720px;left:0;width:1200px;height:480px;background:linear-gradient(180deg,#fafafa,#eceeef)}
.intro-mark{left:200px;top:130px;width:230px;height:230px;background:#dfe4e8}
.eyebrow{left:553px;top:140px;font-family:"Roboto",sans-serif;font-size:16px;letter-spacing:2px;color:var(--muted)}
.intro h2{left:553px;top:172px;width:480px;font-size:27px;font-weight:500;line-height:35px;color:var(--dark)}
.intro p{left:553px;top:288px;width:470px;font-size:14px;line-height:22px;color:var(--muted)}
.intro .btn{left:553px;top:370px;padding:9px 22px;font-size:14px}

/* one stop */
.onestop{top:1200px;left:0;width:1200px;height:760px}
.onestop h2{top:80px;width:1200px;text-align:center;font-size:36px;font-weight:500;line-height:48px;color:#fff}
.tile{width:212px;height:212px;background:#fff;transform:rotate(45deg);box-shadow:0 10px 24px rgba(0,0,0,.45)}
.tile-text{width:200px;text-align:center;font-size:15px;line-height:21px;color:var(--dark)}

/* process */
.process{top:1960px;left:0;width:1200px;height:940px;background:#fff}
.process h2{top:180px;width:1200px;text-align:center;font-size:34px;font-weight:500;color:var(--dark)}
.badge{width:64px;height:64px;background:var(--dark);transform:rotate(45deg)}
.badge-label{width:90px;text-align:center;color:#fff;font-family:"Roboto",sans-serif;font-size:13px;line-height:15px;font-weight:500}
.step{border:1px dashed #9a9a9a;background:#fff;padding:14px 16px;font-size:13px}
.step h3{font-size:15px;font-weight:700;margin-bottom:10px;color:var(--dark)}
.step ul{padding-left:18px;color:var(--ink);line-height:20px}

/* audience */
.audience{top:2900px;left:0;width:1200px;height:600px;background:var(--light)}
.tabs{top:180px;left:185px;display:flex;gap:20px}
.tab{background:#d6d8d9;color:var(--dark);font-size:16px;padding:14px 42px;display:flex;align-items:center;gap:10px}
.tab.active{background:var(--orange);color:#fff}
.tab i{width:16px;height:14px;border:2px solid currentColor;border-radius:3px}
.aud-photo{top:280px;left:188px;width:345px;height:260px;background:linear-gradient(160deg,#f4efe8,#e8d7c4 50%,#c9ccc6)}
.aud-copy{top:290px;left:592px;width:420px}
.aud-copy h3{font-size:18px;font-weight:500;margin-bottom:24px;color:var(--dark)}
.checks{list-style:none}
.checks li{display:flex;gap:14px;font-size:14px;line-height:21px;margin-bottom:22px;color:var(--ink)}
.checks svg{flex:none;margin-top:2px}

/* contact */
.contact{top:3500px;left:0;width:1200px;height:450px;background:#fff}
.contact h2{top:100px;left:320px;font-size:30px;font-weight:400;color:var(--dark)}
.field{height:38px;border:1px solid #bdbdbd;font-size:13px;color:#8a8a8a;padding:10px 12px}
.contact .btn{top:375px;left:518px;padding:12px 46px}

/* footer */
.site-footer{top:3950px;left:0;width:1200px;height:338px;background:var(--darker);color:#cfcfcf}
.footer-brand{left:130px;top:115px;display:flex;align-items:center;gap:10px;font-size:26px;font-weight:500;letter-spacing:5px;color:#fff}
.footer-brand .mark{width:18px;height:18px;background:var(--orange)}
.social{left:142px;top:172px;display:flex;gap:12px}
.social span{width:22px;height:22px;border-radius:50%;background:#9a9a9a}
.foot-col h4{font-family:"Roboto",sans-serif;font-size:15px;font-weight:500;color:#fff;margin-bottom:16px}
.foot-col li{list-style:none;font-size:13px;line-height:21px}
.contact-line{display:flex;gap:10px;font-size:13px;line-height:19px;margin-bottom:12px}
.foot-col p{font-size:13px;line-height:20px}
.foot-col .btn{margin-top:22px;padding:12px 28px;font-size:15px}
.footer-bottom{left:0;top:268px;width:1200px;border-top:1px solid #3d3d3d;padding:22px 120px;display:flex;justify-content:space-between;font-size:12px;color:#aaa}
</style>
</head>
<body>
<div class="page">

<header class="site-header abs">
  <div class="brand"><span class="mark"></span>LARKSPUR</div>
  <nav class="main-nav"><span>HOME</span><span>PRODUCTS</span><span>TECHNOLOGY</span><span>BENEFITS</span><span>MARKETING</span><span>PROCESS</span><span>CASE STUDY</span></nav>
  <a class="btn header-cta">CONTACT</a>
</header>

<section class="hero abs" role="img" aria-label="Photo of a senior living community with two-storey homes, lawns, street lamps and residents walking under a bright sky">
  <h1 class="hero-title abs">Customized Solutions</h1>
  <div class="hero-sub abs">Senior Living Communities Centered on Safety &amp; Efficiency</div>
  <a class="btn hero-btn abs">Learn More</a>
  <div class="arrow abs" style="left:150px"><svg width="44" height="44"><path d="M25 14 L17 22 L25 30" fill="none" stroke="#fff" stroke-width="3"/></svg></div>
  <div class="arrow abs" style="left:1004px"><svg width="44" height="44"><path d="M19 14 L27 22 L19 30" fill="none" stroke="#fff" stroke-width="3"/></svg></div>
</section>

<section class="intro abs">
  <div class="intro-mark abs" role="img" aria-label="Larkspur brand emblem"></div>
  <div class="eyebrow abs">CUSTOM . TURNKEY . SOLUTIONS</div>
  <h2 class="abs">Building safe environments that encourage socialization and improve resident health outcomes.</h2>
  <p class="abs">Brightwell Design provides custom, affordable, easily installed equipment and technology to improve infection control procedures and increased safety for residents, staff, and families.</p>
  <a class="btn abs">Learn More &nbsp;→</a>
</section>

<section class="onestop abs">
  <svg class="abs" style="left:0;top:0" width="1200" height="760">
    <polygon points="0,50 600,0 1200,50 1200,760 0,760" fill="#333333"/>
    <polyline points="0,50 600,0 1200,50" fill="none" stroke="#f0592a" stroke-width="6"/>
  </svg>
  <h2 class="abs">One Stop Shop To<br>Revolutionize Your Business</h2>

  <div class="tile abs" style="left:194px;top:330px"></div>
  <div class="tile abs" style="left:534px;top:250px"></div>
  <div class="tile abs" style="left:414px;top:490px"></div>
  <div class="tile abs" style="left:754px;top:490px"></div>

  <svg class="abs" style="left:284px;top:376px" width="32" height="32"><rect x="4" y="8" width="24" height="20" fill="#333"/><rect x="9" y="13" width="4" height="4" fill="#fff"/><rect x="19" y="13" width="4" height="4" fill="#fff"/><rect x="13" y="20" width="6" height="8" fill="#fff"/><rect x="10" y="3" width="12" height="5" fill="#333"/></svg>
  <div class="tile-text abs" style="left:200px;top:421px">Operational expense and staffing efficiency</div>

  <svg class="abs" style="left:624px;top:296px" width="32" height="34"><path d="M16 2 L29 7 V17 C29 25 23 30 16 32 C9 30 3 25 3 17 V7 Z" fill="#333"/><circle cx="16" cy="17" r="5" fill="#fff"/></svg>
  <div class="tile-text abs" style="left:540px;top:340px">Safety and inspection control for residents, family, friends &amp; staff</div>

  <svg class="abs" style="left:504px;top:536px" width="34" height="32"><circle cx="10" cy="10" r="6" fill="#333"/><circle cx="24" cy="16" r="6" fill="#333"/><circle cx="12" cy="26" r="5" fill="#333"/></svg>
  <div class="tile-text abs" style="left:420px;top:580px">Positive market perceptions shift marketing strategy</div>

  <svg class="abs" style="left:844px;top:536px" width="32" height="32"><path d="M4 28 C4 12 14 4 28 4 C28 18 20 28 4 28 Z" fill="#333"/><path d="M4 28 L20 12" stroke="#fff" stroke-width="2"/></svg>
  <div class="tile-text abs" style="left:760px;top:580px">Energy and environmental efficiency</div>
</section>

<section class="process abs">
  <h2 class="abs">We make it easy</h2>
  <svg class="abs" style="left:0;top:0" width="1200" height="940">
    <path d="M60 470 Q580 230 1140 470" fill="none" stroke="#cfcfcf" stroke-width="1.5"/>
    <path d="M190 720 Q580 640 1010 720" fill="none" stroke="#cfcfcf" stroke-width="1.5"/>
  </svg>

  <div class="badge abs" style="left:216px;top:368px"></div>
  <div class="badge-label abs" style="left:203px;top:386px">1<br>WEEK</div>
  <div class="badge abs" style="left:536px;top:296px"></div>
  <div class="badge-label abs" style="left:523px;top:314px">2<br>WEEK</div>
  <div class="badge abs" style="left:888px;top:368px"></div>
  <div class="badge-label abs" style="left:875px;top:386px">2-3<br>WEEK</div>
  <div class="badge abs" style="left:380px;top:700px"></div>
  <div class="badge-label abs" style="left:367px;top:718px">3-4<br>DAYS</div>
  <div class="badge abs" style="left:728px;top:700px"></div>
  <div class="badge-label abs" style="left:715px;top:718px">3-4<br>DAYS</div>

  <div class="step abs" style="left:140px;top:488px;width:280px;height:150px">
    <h3>Consultation</h3>
    <ul><li>Discuss operational goals &amp; Brightwell custom offerings</li><li>Review existing building documentation</li></ul>
  </div>
  <div class="step abs" style="left:460px;top:400px;width:300px;height:150px">
    <h3>Customized Plan Generation</h3>
    <ul><li>Visit building create custom scope</li><li>Determine project schedule</li><li>Execute contract</li></ul>
  </div>
  <div class="step abs" style="left:800px;top:488px;width:272px;height:170px">
    <h3>Execution &amp; Procurement</h3>
    <ul><li>Order materials</li><li>Receive panels &amp; equipment</li><li>Coordinate storage for varying lead times</li></ul>
  </div>
  <div class="step abs" style="left:320px;top:820px;width:280px;height:100px">
    <h3>Installation</h3>
    <ul><li>Install schedule tailored to building &amp; operational needs</li></ul>
  </div>
  <div class="step abs" style="left:660px;top:820px;width:300px;height:110px">
    <h3>Operations Training</h3>
    <ul><li>Consumer after install</li><li>Track logs</li><li>Follow up as needed</li></ul>
  </div>
</section>

<section class="audience abs">
  <div class="tabs abs">
    <div class="tab"><i></i>Residents</div>
    <div class="tab active"><i></i>Family &amp; Friends</div>
    <div class="tab"><i></i>Staff</div>
    <div class="tab"><i></i>Owners / Corporate</div>
  </div>
  <div class="aud-photo abs" role="img" aria-label="Photo of a smiling multi-generation family: grandparents with their daughter and grandchild"></div>
  <div class="aud-copy abs">
    <h3>Family &amp; Friends</h3>
    <ul class="checks">
      <li><svg width="18" height="18"><circle cx="9" cy="9" r="8" fill="none" stroke="#777" stroke-width="1.5"/><path d="M5 9 L8 12 L13 6" fill="none" stroke="#777" stroke-width="1.5"/></svg>Reduce feelings of guilt when a loved one chooses a senior living setting</li>
      <li><svg width="18" height="18"><circle cx="9" cy="9" r="8" fill="none" stroke="#777" stroke-width="1.5"/><path d="M5 9 L8 12 L13 6" fill="none" stroke="#777" stroke-width="1.5"/></svg>Peace of mind</li>
      <li><svg width="18" height="18"><circle cx="9" cy="9" r="8" fill="none" stroke="#777" stroke-width="1.5"/><path d="M5 9 L8 12 L13 6" fill="none" stroke="#777" stroke-width="1.5"/></svg>Convenience (virtual "shopping" platform)<br>Promote safe &amp; healthy visits</li>
    </ul>
  </div>
</section>

<section class="contact abs">
  <h2 class="abs">Get In Touch</h2>
  <div class="field abs" style="left:320px;top:140px;width:270px">Name</div>
  <div class="field abs" style="left:600px;top:140px;width:270px">Business</div>
  <div class="field abs" style="left:320px;top:196px;width:270px">Email</div>
  <div class="field abs" style="left:600px;top:196px;width:270px">Phone</div>
  <div class="field abs" style="left:320px;top:252px;width:550px;height:100px">How can we help?</div>
  <a class="btn abs">Send Now</a>
</section>

<footer class="site-footer abs">
  <div class="footer-brand abs"><span class="mark"></span>LARKSPUR</div>
  <div class="social abs"><span></span><span></span><span></span></div>

  <div class="foot-col abs" style="left:362px;top:40px;width:220px">
    <h4>Contact Us</h4>
    <div class="contact-line"><svg width="12" height="16"><path d="M6 1 C2.5 1 1 3.5 1 6 C1 9.5 6 15 6 15 C6 15 11 9.5 11 6 C11 3.5 9.5 1 6 1 Z" fill="#cfcfcf"/></svg><span>18 Harbor Lane Suite 4B<br>Fairview CA 90210</span></div>
    <div class="contact-line"><svg width="14" height="14"><path d="M3 1 L6 1 L7 4 L5 6 C6 8 8 10 10 11 L12 9 L14 10 L14 13 C8 13 1 7 1 3 Z" fill="#cfcfcf"/></svg><span>(555) 010-4482</span></div>
    <div class="contact-line"><svg width="14" height="12"><rect x="0.5" y="1.5" width="13" height="9" fill="none" stroke="#cfcfcf"/><path d="M1 2 L7 7 L13 2" fill="none" stroke="#cfcfcf"/></svg><span>hello@larkspur.example</span></div>
  </div>

  <div class="foot-col abs" style="left:620px;top:40px;width:140px">
    <h4>Company</h4>
    <ul><li>Products</li><li>Technology</li><li>Benefits</li><li>Marketing</li><li>Process</li><li>Case Study</li><li>Contact Us</li></ul>
  </div>

  <div class="foot-col abs" style="left:805px;top:40px;width:250px">
    <h4>Still have questions?</h4>
    <p>Contact us using this form, a representative will answer your questions as soon as possible.</p>
    <a class="btn">Get In Touch &nbsp;→</a>
  </div>

  <div class="footer-bottom abs"><span>Copyright 2020 Larkspur. All Rights Reserved.</span><span>Privacy Policy &nbsp;|&nbsp; Terms Of Services</span></div>
</footer>

</div>
</body>
</html>
```